Business Card Design Project

Company name KD MOTOR SERVICES
KD MOTOR
name of owner: Dario Venn
Phone: 604-555-0187
Email: info@kdmotorworks.example
website: www.kdmotorworks.example
Address
24917 51 Ave Surrey, BC V5Q 8K3

Black Back round

Business

```html
<!DOCTYPE html>
<html lang="en">
<head>
<meta charset="utf-8">
<title>KD Motor Services – Business Card</title>
<link href="https://fonts.googleapis.com/css2?family=Open+Sans:wght@400&display=swap" rel="stylesheet">
<style>
  :root {
    --backdrop-top: #f4f4f4;
    --backdrop-bottom: #7d7d7d;
    --card-dark: #161616;
    --card-mid: #2e2e2e;
    --ink: #f2f2f2;
    --line: #cfcfcf;
    --shape-tone: #3a3a3a;
  }
  * { margin: 0; padding: 0; box-sizing: border-box; }
  html, body { width: 695px; height: 1200px; overflow: hidden; }
  body {
    position: relative;
    background: linear-gradient(to bottom, var(--backdrop-top) 0%, #e6e6e6 35%, var(--backdrop-bottom) 100%);
    font-family: "Open Sans", Arial, sans-serif;
    color: var(--ink);
  }
  .card {
    position: absolute;
    left: 89px;
    width: 529px;
    background: radial-gradient(ellipse at 50% 35%, var(--card-mid) 0%, var(--card-dark) 80%);
    box-shadow: 0 2px 6px rgba(0,0,0,0.25);
    overflow: hidden;
  }
  .card--front { top: 166px; height: 325px; }
  .card--back { top: 646px; height: 321px; }

  .front__speed-line {
    position: absolute;
    left: 14px; top: 301px;
    width: 260px; height: 1px;
    background: linear-gradient(to right, rgba(207,207,207,0), var(--line));
  }
  .front__car-illustration {
    position: absolute;
    left: 250px; top: 206px;
    width: 266px; height: 100px;
    background: linear-gradient(to bottom, var(--shape-tone), rgba(58,58,58,0.4));
    border-radius: 60% 40% 8px 8px / 80% 70% 8px 8px;
  }
  .front__company {
    position: absolute;
    left: 36px; top: 252px;
    font-size: 20px;
    letter-spacing: 0.3px;
    white-space: nowrap;
  }

  .back__owner {
    position: absolute;
    right: 68px; top: 46px;
    font-size: 25px;
    letter-spacing: 0.3px;
    text-transform: uppercase;
  }
  .back__contacts {
    position: absolute;
    left: 34px; top: 174px;
    list-style: none;
  }
  .contact {
    display: flex;
    align-items: center;
    height: 34px;
    font-size: 17px;
    white-space: nowrap;
  }
  .contact__icon {
    width: 20px; height: 20px;
    margin-right: 23px;
    flex: none;
  }
</style>
</head>
<body>
  <section class="card card--front" aria-label="Card front">
    <div class="front__speed-line"></div>
    <div class="front__car-illustration" role="img" aria-label="Line illustration of a sports car in side view"></div>
    <p class="front__company">KD MOTOR SERVICES</p>
  </section>

  <section class="card card--back" aria-label="Card back">
    <h1 class="back__owner">Dario Venn</h1>
    <ul class="back__contacts">
      <li class="contact">
        <svg class="contact__icon" viewBox="0 0 20 20" aria-hidden="true"><path fill="#f2f2f2" d="M4 2.5l3 .2 1.3 3.8-2 1.4c1 2.3 2.6 3.9 4.8 4.9l1.4-2 3.8 1.3.2 3c-.2.8-1 1.4-2 1.4C8.600 16.500 3.500 11.400 3 5c0-1 .3-2 1-2.5z"/></svg>
        <span>604-555-0187</span>
      </li>
      <li class="contact">
        <svg class="contact__icon" viewBox="0 0 20 20" aria-hidden="true"><rect x="2.5" y="4.5" width="15" height="11" fill="none" stroke="#f2f2f2" stroke-width="2"/><path d="M3 5l7 6 7-6" fill="none" stroke="#f2f2f2" stroke-width="1.8"/></svg>
        <span>info@kdmotorworks.example</span>
      </li>
      <li class="contact">
        <svg class="contact__icon" viewBox="0 0 20 20" aria-hidden="true"><path fill="none" stroke="#f2f2f2" stroke-width="2" d="M10 18s-5.500-6-5.500-10a5.500 5.500 0 0111 0c0 4-5.500 10-5.500 10z"/><circle cx="10" cy="8" r="2" fill="#f2f2f2"/></svg>
        <span>www.kdmotorworks.example</span>
      </li>
      <li class="contact">
        <svg class="contact__icon" viewBox="0 0 20 20" aria-hidden="true"><rect x="3" y="3.5" width="14" height="13" fill="none" stroke="#f2f2f2" stroke-width="2"/></svg>
        <span>24917 51 Ave Surrey, BC V5Q 8K3</span>
      </li>
    </ul>
  </section>
</body>
</html>
```